Create a pouch design for a new sports supplement product

Dimensions are 235mm (width) x 335mm (length) x 110mm (gusset)
File 1 - Extension of design brief please read both briefs
File 2 - Is 2 potential pouches this is just to give you a better example of size the dimensions are for the pouch on the right. This picture is not to give you design ideas as I am not very keen on either of these designs.
We need a design to be printed onto the pouches of our whey protein product. The brand name is 'Brisk Fuelworks' and needs to be displayed on the packaging either just writing or a simple logo design. I am not the most creative person in the world but have put together a more detailed brief listing some of the key information that needs to be included on the pouch (See attachment) Please feel free if you have experience of this the sports supplement market or have different ideas then please feel free to explore them.
The pouch would either be printed straight onto the pouch, or possibly just a printed label (front & back) to be stuck onto the pouch. Please design either or both.
Open to different colour schemes. Design has to be modern looking and eye-catching.
Some key points;
High quality whey protein concentrate
All Natural
Soy free
Great tasting
Please google image search 'protein pouches' to see other designs if your not familiar with the sports supplement market.
Any questions feel free to ask.
Updates
Project Deadline Extended
Reason: give me chance to give feedback
Hi, Thanks for all your design! I am really busy at the moment so haven't had chance to give feedback and have a proper look through all the designs. I have extended the time frame to give myself chance to give proper feedback and see any changes needed. Expect feedback sunday at the latest, and I will be pick a design early next week.
Target Market(s)
Sports supplement market. Product is a whey protein shake
Industry/Entity Type
Nutrition
Look and feel
Each slider illustrates characteristics of the customer's brand and the style your logo design should communicate.

```html
<!DOCTYPE html>
<html lang="en">
<head>
<meta charset="utf-8">
<title>Brisk Fuelworks – Natural Whey Protein Pouch</title>
<link rel="stylesheet" href="https://fonts.googleapis.com/css2?family=Josefin+Sans:wght@300;400&family=Montserrat:wght@400;500;700;800&display=swap">
<style>
  :root {
    --page: #ffffff;
    --pouch: #0b0b0b;
    --white: #ffffff;
    --ink: #111111;
    --blue: #00aeef;
    --green: #8dc63f;
    --yellow: #fff44f;
    --cream: #fffabf;
    --berry: #e8145a;
    --berry-dark: #b3122a;
  }
  * { margin: 0; padding: 0; box-sizing: border-box; }
  html, body { width: 1200px; height: 1000px; overflow: hidden; background: var(--page); }
  .canvas { position: relative; width: 1200px; height: 1000px; }

  .pouch {
    position: absolute; left: 350px; top: 70px; width: 530px; height: 880px;
    background: var(--pouch); border-radius: 14px 14px 10px 10px;
  }
  .tear-line { position: absolute; left: 350px; top: 122px; width: 530px; height: 12px; }
  .tear-label {
    position: absolute; left: 357px; top: 108px; font: 400 9px "Montserrat", sans-serif;
    color: var(--white); letter-spacing: .3px;
  }

  .brand { position: absolute; left: 446px; top: 220px; color: var(--white); font-family: "Josefin Sans", sans-serif; }
  .brand-name { font-size: 56px; font-weight: 400; line-height: 1; letter-spacing: 1px; }
  .brand-sub { font-size: 12px; font-weight: 400; letter-spacing: 4.6px; margin-top: 17px; }

  .tile { position: absolute; width: 160px; height: 160px; border-radius: 3px; color: var(--ink); }
  .tile-protein { left: 442px; top: 335px; background: var(--blue); padding: 50px 0 0 14px; }
  .tile-flavours { left: 442px; top: 500px; background: var(--green); padding: 72px 0 0 12px; }
  .tile-amino { left: 608px; top: 465px; background: var(--yellow); padding: 100px 10px 0 0; text-align: right; }
  .tile-soy { left: 608px; top: 630px; background: var(--cream); padding: 98px 10px 0 0; text-align: right; }

  .bold { font-family: "Montserrat", sans-serif; font-weight: 800; line-height: 1; }
  .medium { font-family: "Montserrat", sans-serif; font-weight: 500; line-height: 1; }
  .light { font-family: "Josefin Sans", sans-serif; font-weight: 300; line-height: 1; }
  .small { font-family: "Montserrat", sans-serif; font-weight: 400; line-height: 1.15; }

  .vertical {
    position: absolute; writing-mode: vertical-rl; transform: rotate(180deg);
    line-height: 1; white-space: nowrap; z-index: 2;
  }
  .v-natural { left: 617px; top: 338px; color: var(--green); font: 300 26px "Josefin Sans", sans-serif; letter-spacing: 0.5px; }
  .v-whey { left: 647px; top: 206px; color: var(--yellow); font: 800 72px "Montserrat", sans-serif; letter-spacing: -1px; }
  .v-protein { left: 720px; top: 226px; color: var(--blue); font: 700 33px "Montserrat", sans-serif; letter-spacing: 8px; }

  .flavour-art {
    position: absolute; left: 465px; top: 670px; width: 110px; height: 84px; border-radius: 40px 40px 45px 45px;
    background: radial-gradient(circle at 45% 40%, #f04a4a, var(--berry-dark) 70%);
  }
  .flavour-name {
    position: absolute; left: 470px; top: 760px; width: 119px; text-align: right;
    font: 400 10.5px "Montserrat", sans-serif; letter-spacing: 4px; color: var(--berry); line-height: 17px;
  }
  .net-weight { position: absolute; left: 650px; top: 812px; color: var(--white); font: 700 11px "Montserrat", sans-serif; }
  .website { position: absolute; left: 652px; top: 829px; color: var(--white); font: 400 8px "Montserrat", sans-serif; }
</style>
</head>
<body>
<div class="canvas">
  <div class="pouch"></div>

  <svg class="tear-line" viewBox="0 0 530 12" aria-hidden="true">
    <line x1="0" y1="6" x2="462" y2="6" stroke="#ffffff" stroke-width="1.5" stroke-dasharray="4 5"/>
    <g fill="none" stroke="#ffffff" stroke-width="1.4">
      <circle cx="503" cy="2.5" r="2.5"/>
      <circle cx="503" cy="9.5" r="2.5"/>
      <line x1="501" y1="4" x2="468" y2="10"/>
      <line x1="501" y1="8" x2="468" y2="2"/>
    </g>
  </svg>
  <div class="tear-label">TEAR HEAR</div>

  <div class="brand">
    <div class="brand-name">BRISK</div>
    <div class="brand-sub">FUELWORKS</div>
  </div>

  <div class="tile tile-protein">
    <div class="bold" style="font-size:36px">80%</div>
    <div class="medium" style="font-size:21px;margin-top:1px">HIGH</div>
    <div class="small" style="font-size:10px">QUALITY</div>
    <div class="bold" style="font-size:16px">PROTEIN</div>
    <div class="small" style="font-size:9px">CONCENTRATE</div>
  </div>

  <div class="tile tile-flavours">
    <div class="bold" style="font-size:23px">NO</div>
    <div class="light" style="font-size:26px;margin-top:2px">ARTIFICIAL</div>
    <div class="light" style="font-size:19px;margin-top:1px;text-align:right;padding-right:6px">FLAVOURS</div>
  </div>

  <div class="tile tile-amino">
    <div class="light" style="font-size:21px">EXCELLENT</div>
    <div class="bold" style="font-size:14px;margin-top:2px">AMINO ACID</div>
    <div class="small" style="font-size:8px;margin-top:1px">PROFILE</div>
  </div>

  <div class="tile tile-soy">
    <div class="light" style="font-size:25px">SOY</div>
    <div class="bold" style="font-size:21px;margin-top:2px">FREE</div>
  </div>

  <div class="vertical v-natural">NATURAL</div>
  <div class="vertical v-whey">WHEY</div>
  <div class="vertical v-protein">PROTEIN</div>

  <div class="flavour-art" role="img" aria-label="Two ripe strawberries with green leaves"></div>
  <div class="flavour-name">STRAWBERRY<br>FLAVOUR</div>

  <div class="net-weight">909g 30 servings</div>
  <div class="website">www.briskfuelworks.com</div>
</div>
</body>
</html>
```